Frostvel.io - Polar Expeditions Specialists

We need a modern, visually striking business card for Frostvel.io, a company specialized in selling expedition cruises to the most remote regions on Earth, with a focus on the Arctic and Antarctica. The design should instantly communicate that the cardholder is an expert in polar travel. Use clean, premium aesthetics with cool tones like icy blue and white, possibly incorporating polar imagery (ice, glaciers, penguins, etc.)

Contact Information for Business Card

Feels high-end and trustworthy.. Visually memorable — encourages people to keep it

Colors
0054AA
0677BA
7BADD7
CADEEF
E8F1F8

Requirements
Must have
• ice, glaciers, penguins, montains
Nice to have
• modern, transparente,

```html
<!DOCTYPE html>
<html lang="en">
<head>
<meta charset="utf-8">
<title>Frostvel.io — Business Card</title>
<link href="https://fonts.googleapis.com/css2?family=Poppins:wght@400;600;700&display=swap" rel="stylesheet">
<style>
  :root {
    --page-bg: #e6e8eb;
    --card-dark: #0e0c22;
    --grad-light: #2e72ad;
    --grad-mid: #1b3f6e;
    --grad-dark: #0d1a3a;
    --ink-white: #ffffff;
    --ink-soft: #c9cbd8;
    --card-shadow: rgba(10, 14, 30, 0.28);
  }
  * { margin: 0; padding: 0; box-sizing: border-box; }
  html, body {
    width: 1200px; height: 800px; overflow: hidden;
    background: var(--page-bg);
    font-family: "Poppins", sans-serif;
  }
  .canvas { position: relative; width: 1200px; height: 800px; }
  .card {
    position: absolute; left: 390px; width: 420px; height: 270px;
    box-shadow: 0 6px 18px var(--card-shadow);
    overflow: hidden; color: var(--ink-white);
  }
  .card-front { top: 100px; background: var(--card-dark); }
  .card-back {
    top: 400px;
    background: linear-gradient(215deg, var(--grad-light) 0%, var(--grad-mid) 50%, var(--grad-dark) 100%);
  }
  .holder { position: absolute; left: 34px; top: 84px; }
  .holder-name { font-size: 16px; font-weight: 600; letter-spacing: 0.04em; text-transform: uppercase; }
  .holder-role { font-size: 10.5px; font-weight: 400; color: var(--ink-soft); margin-top: 2px; }
  .contact-list { list-style: none; margin-top: 22px; }
  .contact-item {
    display: flex; align-items: center; gap: 9px;
    font-size: 10.5px; color: var(--ink-soft); height: 18px;
  }
  .contact-icon { width: 10px; height: 10px; flex: none; }
  .front-brand {
    position: absolute; right: 30px; top: 118px;
    display: flex; align-items: center; gap: 8px;
    font-size: 24px; font-weight: 600; color: var(--ink-white);
  }
  .brand-dot { width: 12px; height: 12px; border-radius: 50%; background: var(--ink-white); }
  .back-lockup {
    position: absolute; inset: 0;
    display: flex; flex-direction: column; align-items: center; justify-content: center;
    padding-top: 20px;
  }
  .back-mark { width: 30px; height: 30px; border-radius: 50%; background: var(--ink-white); margin-bottom: 14px; }
  .back-name { font-size: 34px; font-weight: 600; line-height: 1; }
  .back-tagline { font-size: 10px; font-weight: 600; margin-top: 8px; }
</style>
</head>
<body>
<main class="canvas">
  <section class="card card-front">
    <div class="holder">
      <h1 class="holder-name">Marcus Ellery</h1>
      <p class="holder-role">Owner</p>
      <ul class="contact-list">
        <li class="contact-item">
          <svg class="contact-icon" viewBox="0 0 10 10"><rect x="2.5" y="0.5" width="5" height="9" rx="1" fill="none" stroke="#c9cbd8" stroke-width="1"/><circle cx="5" cy="7.8" r="0.6" fill="#c9cbd8"/></svg>
          550 314 772
        </li>
        <li class="contact-item">
          <svg class="contact-icon" viewBox="0 0 10 10"><rect x="0.5" y="2" width="9" height="6.5" rx="0.8" fill="#c9cbd8"/><path d="M0.8 2.4 L5 5.6 L9.2 2.4" fill="none" stroke="#0e0c22" stroke-width="0.9"/></svg>
          hello@frostvel.io
        </li>
        <li class="contact-item">
          <svg class="contact-icon" viewBox="0 0 10 10"><circle cx="5" cy="5" r="4.3" fill="none" stroke="#c9cbd8" stroke-width="0.9"/><ellipse cx="5" cy="5" rx="1.8" ry="4.3" fill="none" stroke="#c9cbd8" stroke-width="0.8"/><line x1="0.7" y1="5" x2="9.3" y2="5" stroke="#c9cbd8" stroke-width="0.8"/></svg>
          www.frostvel.io
        </li>
      </ul>
    </div>
    <div class="front-brand"><span class="brand-dot"></span>Frostvel.io</div>
  </section>

  <section class="card card-back">
    <div class="back-lockup">
      <span class="back-mark"></span>
      <h2 class="back-name">Frostvel.io</h2>
      <p class="back-tagline">Polar Expeditions Specialists</p>
    </div>
  </section>
</main>
</body>
</html>
```